female esthetician looking for an impact business card

I an an expert in skin care industry with high experience in NYC.I want my business card to look professional , an impact at first look. I do want a combination between white and gold . I believe the font will be great if is gold.. The Fonts are also important. MARISELA VONDRAKE (SKIN CARE BOUTIQUE)

THIS SHOULD BE THE BUSINESS NAME, and should be placed on th eback of the card.
IN front m, the name MARISELA VONDRAKE - ESTHETCIAN

BY APPOINTMENTS ONLY: 555.218.9031

Target Market(s)

HIGH END CLIENTELE

Contact Information for Business Card

iT WILL BE on a luxury paper. I neeed the wow feeling

Requirements
Should not have
• pictures

```html
<!DOCTYPE html>
<html lang="en">
<head>
<meta charset="UTF-8">
<title>Marisela Vondrake — Business Card</title>
<link rel="stylesheet" href="https://fonts.googleapis.com/css2?family=Raleway:wght@300;400&display=swap">
<style>
  :root {
    --backdrop: #e9e5dd;
    --card-gold: #cdb128;
    --card-gold-deep: #c5a821;
    --pattern-tone-a: #d6ba2e;
    --pattern-tone-b: #c9ab24;
    --ink-white: #ffffff;
    --card-shadow: rgba(40, 30, 10, 0.45);
  }
  * { box-sizing: border-box; margin: 0; padding: 0; }
  html, body {
    width: 900px;
    height: 1200px;
    overflow: hidden;
  }
  body {
    position: relative;
    background: var(--backdrop);
    font-family: "Raleway", "Helvetica Neue", Arial, sans-serif;
    color: var(--ink-white);
  }
  .card {
    position: absolute;
    left: 81px;
    width: 810px;
    border-radius: 48px 12px 48px 12px;
    overflow: hidden;
    box-shadow: 0 8px 14px var(--card-shadow);
  }
  .card--front {
    top: 126px;
    height: 459px;
    background: var(--card-gold);
  }
  .card--back {
    top: 636px;
    height: 429px;
    background: var(--card-gold-deep);
  }
  .card__pattern {
    position: absolute;
    inset: 0;
    background: radial-gradient(ellipse at 50% 45%, var(--pattern-tone-a), var(--pattern-tone-b));
  }
  .front__identity {
    position: absolute;
    left: 0;
    right: 0;
    top: 168px;
    text-align: center;
  }
  .front__name {
    font-weight: 400;
    font-size: 44px;
    letter-spacing: 3px;
    line-height: 1;
  }
  .front__title {
    margin-top: 14px;
    font-weight: 400;
    font-size: 16px;
    letter-spacing: 5px;
    text-transform: uppercase;
  }
  .back__contact {
    position: absolute;
    left: 0;
    right: 0;
    top: 175px;
    text-align: center;
    font-weight: 300;
    line-height: 1.3;
  }
  .back__phone { font-size: 30px; letter-spacing: 1px; }
  .back__email { font-size: 29px; }
</style>
</head>
<body>
  <section class="card card--front">
    <div class="card__pattern" role="img" aria-label="Tone-on-tone gold damask floral pattern covering the card face"></div>
    <div class="front__identity">
      <h1 class="front__name">MARISELA VONDRAKE</h1>
      <p class="front__title">Skin Care Expert</p>
    </div>
  </section>

  <section class="card card--back">
    <div class="back__contact">
      <p class="back__phone">555-218-903</p>
      <p class="back__email">mariselavondrake@mailbox.com</p>
    </div>
  </section>
</body>
</html>
```